Redesign of Plastic Surgeon Website to fully responsive / modern feel

Hi

Our current website is out of date www.harbourlinecosmetic.org

We want a fresh / modern looking design
Needs to be fully responsive design that works extremely well on ipad and mobile device

Would like design for both full screen website and mobile

Have listed a few websites of other plastic surgeons we like
http://www.reformclinicplus.com/
http://www.doriankeelermd.com/
http://www.tarrantcontours.com/
http://www.oakdenecosmeticsurgery.com/

Menu needs to include
1. About Us
2. Procedures (see current website for example)
3. News
4. Patient Resources
5. Contact Us

We are flexible with colours / images / layout

I have uploaded a document that has some content - the face pages content is completed only

some of the procedures can have content upwards of 4000 words - total website can be large with over 40,000 words
Updates

Hi I have updated the logo for our design for the new website - this is the logo and colours we want reflected throughout the siteThanks Added Wednesday, January 13, 2016

Target Market(s)

Mainly women 20-60 85% of practice
Some men 15%

Industry/Entity Type

Plastic Surgery

Number of Pages Required

5+ page

Requirements
Must have
• We need designs for
• Homepage
• Internal pages
• 1. Landing pages for breast / body / face / non surgical main pages
• 2. Procedure pages for individual pages under each section - eg breast augmentation
• 3. About us pages - like meet the doctor, our staff, clinics
• 4. Contact page
• 5. Blog / News page
Nice to have
• See our list of websites for examples of designs we like
• Like full screen design with nice hero image
• Needs to have good to call to action messages on home page like
• Specials, procedure of the month, etc

```html
<!DOCTYPE html>
<html lang="en">
<head>
<meta charset="utf-8">
<title>Contact Us – Harbourline Cosmetic Institute</title>
<link href="https://fonts.googleapis.com/css2?family=PT+Sans:wght@400;700&family=Raleway:wght@300;400;500&display=swap" rel="stylesheet">
<style>
:root{
  --orange:#d9822b;
  --orange-deep:#d27f2e;
  --ink:#2b2b2b;
  --title:#5a4a3a;
  --grey-bar:#cfcfcf;
  --footer:#2a2626;
  --sand:#d4c39a;
  --mint:#a8e0d4;
  --rust:#d4622a;
  --umber:#5e5040;
  --line:#555;
}
*{box-sizing:border-box;margin:0;padding:0}
html,body{width:1083px;height:1200px;overflow:hidden;background:#fff}
body{position:relative;font-family:"PT Sans",sans-serif;color:var(--ink)}
.abs{position:absolute}

/* header */
.site-header{left:0;top:0;width:1083px;height:110px;background:#fff;box-shadow:0 2px 4px rgba(0,0,0,.08);z-index:2}
.brand-box{left:91px;top:0;width:334px;height:110px;background:#fff;box-shadow:0 0 5px rgba(0,0,0,.15);display:flex;align-items:center;justify-content:center;gap:10px}
.brand-mark{width:14px;height:14px;border-radius:50%;background:var(--orange)}
.brand-name{font-family:"Raleway",sans-serif;font-weight:400;font-size:19px;color:#3a3a3a}
.call-bar{left:669px;top:0;width:335px;height:38px;background:var(--grey-bar);display:flex;align-items:center;padding-left:14px;gap:8px;color:#fff;font-family:"Raleway",sans-serif;font-size:11px;letter-spacing:.3px}
.call-bar strong{color:var(--orange);font-size:18px;font-weight:500;letter-spacing:.5px}
.main-nav{top:80px;left:472px;display:flex;font-size:11px;letter-spacing:.2px;color:#333}
.main-nav span{position:absolute;white-space:nowrap}
.main-nav .active{color:var(--orange)}
.caret{display:inline-block;margin-left:5px;border-left:3.5px solid transparent;border-right:3.5px solid transparent;border-top:4px solid currentColor;vertical-align:2px}

/* title band */
.page-title-band{left:0;top:110px;width:1083px;height:88px;background:linear-gradient(100deg,#f3f3f3 0%,#f3f3f3 70%,#fbfbfb 85%,#efefef 100%)}
.page-title{left:76px;top:134px;font-family:"Raleway",sans-serif;font-weight:300;font-size:30px;color:var(--title)}
.colour-stripe{left:0;top:198px;width:1083px;height:7px;display:flex}
.colour-stripe i{flex:1}

/* contact */
.intro{left:78px;top:244px;font-family:"Raleway",sans-serif;font-size:14.5px;color:#333}
.intro b{font-weight:700}
.field{position:absolute;border:1px solid var(--line);background:#fff;font-size:11px;color:#333;padding:8px 13px}
.send-btn{left:78px;top:445px;width:98px;height:28px;background:var(--orange);color:#fff;font-size:11.5px;display:flex;align-items:center;justify-content:center}

/* associations */
.associations{left:0;top:516px;width:1083px;height:175px;background:linear-gradient(180deg,#eeece6,#f3f1ea 50%,#e4e0d6)}
.badge{position:absolute;background:#c9cbc8}

/* tiles */
.category-tile{position:absolute;top:691px;width:271px;height:217px;display:flex;align-items:center;justify-content:center;color:#fff;font-weight:700;font-size:18px}
.tile-face{left:0;background:radial-gradient(circle at 50% 50%,#a88a75,#4e4a44)}
.tile-breast{left:271px;background:radial-gradient(circle at 50% 40%,#8a5c44,#3b2a22)}
.tile-body{left:542px;background:radial-gradient(circle at 50% 40%,#b07a52,#2e241e)}
.tile-non-surgical{left:812px;width:271px;background:radial-gradient(circle at 40% 50%,#b98a6c,#5a3d2e)}

/* footer */
.site-footer{left:0;top:908px;width:1083px;height:250px;background:linear-gradient(160deg,#2c2828 0%,#262222 60%,#332d2a 100%);color:#fff}
.footer-heading{position:absolute;top:44px;font-family:"Raleway",sans-serif;font-size:20px}
.sitemap{position:absolute;left:77px;top:84px;list-style:none;font-size:12.5px;line-height:19px}
.news-thumb{left:236px;top:84px;width:97px;height:77px;background:linear-gradient(135deg,#f0d2bd,#e0b398);border:2px solid #fff}
.news-title{left:344px;top:86px;color:var(--orange);font-family:"Raleway",sans-serif;font-size:12.5px}
.news-excerpt{left:347px;top:107px;width:209px;font-family:"Raleway",sans-serif;font-size:11px;line-height:13.4px;text-align:justify}
.view-all{left:456px;top:180px;width:98px;height:27px;background:var(--orange);display:flex;align-items:center;justify-content:center;font-size:11px}
.clinic{position:absolute;top:86px;font-size:11px;line-height:13.3px}
.clinic h3{font-weight:400;color:var(--orange);font-size:14px;line-height:16px}

.copyright-bar{left:0;top:1158px;width:1083px;height:42px;background:var(--orange-deep);color:#fff;font-family:"Raleway",sans-serif;font-size:9.5px;display:flex;align-items:center;justify-content:center}
</style>
</head>
<body>

<header class="site-header abs">
  <div class="brand-box abs"><span class="brand-mark"></span><span class="brand-name">Harbourline Cosmetic Institute</span></div>
  <div class="call-bar abs">
    <svg width="16" height="18" viewBox="0 0 24 24" fill="#fff"><path d="M6.6 10.8a15.1 15.1 0 0 0 6.6 6.6l2.2-2.2a1 1 0 0 1 1-.25 11.4 11.4 0 0 0 3.6.57 1 1 0 0 1 1 1V20a1 1 0 0 1-1 1A17 17 0 0 1 3 4a1 1 0 0 1 1-1h3.5a1 1 0 0 1 1 1c0 1.25.2 2.45.57 3.57a1 1 0 0 1-.25 1z"/></svg>
    <span>CALL FOR APPOINTMENTS :</span><strong>02 8000 4172</strong>
  </div>
  <nav class="main-nav abs">
    <span style="left:0">ABOUT US<i class="caret"></i></span>
    <span style="left:99px">PROCEDURES<i class="caret"></i></span>
    <span style="left:204px" class="active">PATIENT RESOURCES<i class="caret"></i></span>
    <span style="left:338px">NEWS / BLOGS</span>
    <span style="left:435px">CONTACT US</span>
  </nav>
</header>

<div class="page-title-band abs"></div>
<h1 class="page-title abs">Contact Us</h1>
<div class="colour-stripe abs"><i style="background:var(--sand)"></i><i style="background:var(--mint)"></i><i style="background:var(--rust)"></i><i style="background:var(--umber)"></i></div>

<p class="intro abs">For all appointments and inquiries, please call <b>(02) 9000 2618</b></p>
<div class="field" style="left:78px;top:288px;width:450px;height:29px">Name</div>
<div class="field" style="left:78px;top:325px;width:450px;height:29px">Number</div>
<div class="field" style="left:78px;top:363px;width:450px;height:29px">Email</div>
<div class="field" style="left:78px;top:400px;width:450px;height:29px">Subject</div>
<div class="field" style="left:553px;top:288px;width:451px;height:140px">Message</div>
<div class="send-btn abs">SEND</div>

<section class="associations abs" role="img" aria-label="Row of professional association membership badges">
  <span class="badge" style="left:77px;top:66px;width:137px;height:40px;border-radius:4px"></span>
  <span class="badge" style="left:236px;top:58px;width:86px;height:56px;border-radius:50%"></span>
  <span class="badge" style="left:354px;top:62px;width:192px;height:50px;border-radius:4px"></span>
  <span class="badge" style="left:562px;top:46px;width:74px;height:82px;border-radius:4px"></span>
  <span class="badge" style="left:660px;top:56px;width:96px;height:60px;border-radius:4px"></span>
  <span class="badge" style="left:778px;top:62px;width:136px;height:48px;border-radius:4px"></span>
  <span class="badge" style="left:926px;top:56px;width:68px;height:68px;border-radius:50%"></span>
</section>

<div class="category-tile tile-face" role="img" aria-label="Portrait photograph for face procedures">Face</div>
<div class="category-tile tile-breast" role="img" aria-label="Photograph for breast procedures">Breast</div>
<div class="category-tile tile-body" role="img" aria-label="Photograph of a bare back for body procedures">Body</div>
<div class="category-tile tile-non-surgical" role="img" aria-label="Portrait photograph for non-surgical treatments">Non-Surgical</div>

<footer class="site-footer abs">
  <h2 class="footer-heading" style="left:77px">Sitemap</h2>
  <h2 class="footer-heading" style="left:235px">Latest News / Blogs</h2>
  <h2 class="footer-heading" style="left:603px">Our Clinic</h2>
  <ul class="sitemap">
    <li>Home</li><li>About Us</li><li>Procedures</li><li>Patient Resources</li><li>News / Blog</li><li>Contact Us</li>
  </ul>
  <div class="news-thumb abs" role="img" aria-label="Photograph of a tummy after weight loss"></div>
  <p class="news-title abs">Who should have a tummy tuck?</p>
  <p class="news-excerpt abs">After giving birth or losing heaps of weight, many women find the shape of their tummy has dramatically changed and, no matter how much cardio ...</p>
  <div class="view-all abs">VIEW ALL</div>
  <div class="clinic" style="left:603px"><h3>Dee Why</h3>120 Harbour Lane, Suite 12<br>Dee Why, NSW 2099</div>
  <div class="clinic" style="left:757px"><h3>Leichardt</h3>Level 1<br>48 Elm Street 2040<br>Tel: 02 8000 4172</div>
  <div class="clinic" style="left:886px"><h3>Newcastle</h3>5/9 Carrow St<br>Merewether, NSW 2291</div>
</footer>

<div class="copyright-bar abs">© Harbourline Cosmetic Institute Dr Leon Ashcroft Plastic Surgery Sydney Australia&nbsp; 2016</div>

</body>
</html>
```